This is for a poster that will be hanging in the window of a Men's Suit Store in the mall:
Size 4 feet wide by 6 feet high
Main point is: A sale on "Suits" or "Men's Suits" at 40%-60% off ( the 40%-60% off should be the focal point)
Some words that can be used are "Sale" or "Clearance Sale"
Some key words that can be used to make it urgent are "limited time offer" or something similar.
You can get creative, the point is for the customer to want to come into the store and buy a suit right away.
You may use a graphic (picture of a man in a suit). It is not necessary but if it looks good you can use it. (If you do use a picture, it should be of a modern fit or slim fit suit)
Sorry, the initial brief somehow got deleted from the project. Please see the updated brief.
Thanks
Reason: Project was closed for some reason, extended to give enough time to complete
Target Market(s)
Mostly Men ages 35-55
Industry/Entity Type
Store
Colors
Designer to choose colors to be used in the design.

```html
<!DOCTYPE html>
<html lang="en">
<head>
<meta charset="UTF-8">
<title>Men's Suit Sale Poster</title>
<link rel="stylesheet" href="https://fonts.googleapis.com/css2?family=Montserrat:wght@900&family=Poppins:wght@500;600&display=swap">
<style>
  :root {
    --page-bg: #ffffff;
    --poster-bg: #000000;
    --band-dark: #0d0d0d;
    --band-mid: #3a3a3a;
    --text-silver: #ececec;
  }
  * { margin: 0; padding: 0; box-sizing: border-box; }
  html, body {
    width: 1200px;
    height: 1000px;
    overflow: hidden;
    background: var(--page-bg);
  }
  .canvas {
    position: relative;
    width: 1200px;
    height: 1000px;
  }
  .poster {
    position: absolute;
    left: 357px;
    top: 140px;
    width: 487px;
    height: 719px;
    background: var(--poster-bg);
    overflow: hidden;
  }
  .poster__headline {
    position: absolute;
    inset: 0;
    width: 487px;
    height: 719px;
  }
  .poster__headline text {
    font-family: "Montserrat", Arial, sans-serif;
    font-weight: 900;
  }
  .poster__product {
    position: absolute;
    left: 0;
    right: 0;
    top: 592px;
    text-align: center;
    font-family: "Poppins", Arial, sans-serif;
    font-weight: 600;
    font-size: 39px;
    line-height: 1.2;
    letter-spacing: -0.5px;
    color: var(--text-silver);
    background: linear-gradient(180deg, #ffffff 0%, #d8d8d8 55%, #9a9a9a 100%);
    -webkit-background-clip: text;
    background-clip: text;
    -webkit-text-fill-color: transparent;
  }
  .poster__urgency-band {
    position: absolute;
    left: 0;
    right: 0;
    bottom: 0;
    height: 57px;
    display: flex;
    align-items: center;
    justify-content: center;
    background: linear-gradient(90deg, var(--band-dark) 0%, var(--band-mid) 50%, var(--band-dark) 100%);
  }
  .poster__urgency-text {
    font-family: "Poppins", Arial, sans-serif;
    font-weight: 600;
    font-size: 37px;
    line-height: 1;
    letter-spacing: -0.5px;
    background: linear-gradient(180deg, #ffffff 0%, #e0e0e0 50%, #9c9c9c 100%);
    -webkit-background-clip: text;
    background-clip: text;
    -webkit-text-fill-color: transparent;
  }
</style>
</head>
<body>
<div class="canvas">
  <section class="poster" aria-label="Men's suit sale poster">
    <svg class="poster__headline" viewBox="0 0 487 719" role="group">
      <defs>
        <linearGradient id="red-face" x1="0" y1="0" x2="0" y2="1">
          <stop offset="0" stop-color="#f2545a"/>
          <stop offset="0.45" stop-color="#d0121b"/>
          <stop offset="1" stop-color="#8c0a10"/>
        </linearGradient>
        <linearGradient id="chrome-side" x1="0" y1="0" x2="1" y2="1">
          <stop offset="0" stop-color="#e6e6e6"/>
          <stop offset="0.5" stop-color="#6a6a6a"/>
          <stop offset="1" stop-color="#2a2a2a"/>
        </linearGradient>
      </defs>

      <g class="headline-word headline-word--sale">
        <text x="252" y="192" font-size="200" text-anchor="middle" textLength="425" lengthAdjust="spacingAndGlyphs" fill="url(#chrome-side)">SALE</text>
        <text x="248" y="187" font-size="200" text-anchor="middle" textLength="425" lengthAdjust="spacingAndGlyphs" fill="url(#chrome-side)">SALE</text>
        <text x="243" y="182" font-size="200" text-anchor="middle" textLength="425" lengthAdjust="spacingAndGlyphs" fill="url(#red-face)">SALE</text>
      </g>

      <g class="headline-figure headline-figure--low">
        <text x="250" y="366" font-size="175" text-anchor="middle" textLength="365" lengthAdjust="spacingAndGlyphs" fill="url(#chrome-side)">40%</text>
        <text x="247" y="363" font-size="175" text-anchor="middle" textLength="365" lengthAdjust="spacingAndGlyphs" fill="url(#chrome-side)">40%</text>
        <text x="243" y="360" font-size="175" text-anchor="middle" textLength="365" lengthAdjust="spacingAndGlyphs" fill="url(#red-face)">40%</text>
      </g>

      <g class="headline-figure headline-figure--high">
        <text x="252" y="566" font-size="215" text-anchor="middle" textLength="350" lengthAdjust="spacingAndGlyphs" fill="url(#chrome-side)">60%</text>
        <text x="246" y="572" font-size="215" text-anchor="middle" textLength="350" lengthAdjust="spacingAndGlyphs" fill="url(#chrome-side)">60%</text>
        <text x="240" y="578" font-size="215" text-anchor="middle" textLength="350" lengthAdjust="spacingAndGlyphs" fill="url(#red-face)">60%</text>
      </g>
    </svg>

    <p class="poster__product">Men’s Suit</p>

    <div class="poster__urgency-band">
      <p class="poster__urgency-text">Limited Time Offer</p>
    </div>
  </section>
</div>
</body>
</html>
```